CSLN Banner

We need a design for a pull-up banner (850 x 2000 mm) to promote the Civic Strand Ledger Norm. https://cslnorm.net/en/
The banner action should be to get people to scan a QR code to join a mailing list (add a frame to add the QR code)

Use the website colours and typology https://cslnorm.net/en/
See also brochure for ideas https://cslnorm.net/documents/9/CSLN_brochure_english.pdf

```html
<!DOCTYPE html>
<html lang="en">
<head>
<meta charset="utf-8">
<title>CSLN Pull-up Banner</title>
<link rel="stylesheet" href="https://fonts.googleapis.com/css2?family=Montserrat:wght@400;600;700&display=swap">
<style>
  :root {
    --page: #ececec;
    --ink-top: #12112a;
    --ink-bottom: #07070f;
    --band: #13122b;
    --white: #ffffff;
    --lime: #c3d62e;
    --blue: #3a8fd6;
    --map-light: #cdeaf6;
    --map-mid: #79c3e3;
  }
  * { box-sizing: border-box; margin: 0; padding: 0; }
  html, body { width: 1200px; height: 1200px; overflow: hidden; }
  body {
    background: var(--page);
    font-family: "Montserrat", sans-serif;
    display: flex;
    align-items: center;
    justify-content: center;
  }
  .banner {
    position: relative;
    width: 490px;
    height: 1150px;
    background: linear-gradient(180deg, var(--ink-top) 0%, #0b0b1c 50%, var(--ink-bottom) 100%);
    color: var(--white);
    box-shadow: 0 6px 18px rgba(0,0,0,0.25);
    overflow: hidden;
  }
  .brand-name {
    position: absolute;
    top: 62px;
    left: 0; right: 0;
    text-align: center;
    font-weight: 600;
    font-size: 132px;
    line-height: 1;
    letter-spacing: -2px;
    color: var(--white);
  }
  .headline {
    position: absolute;
    top: 272px;
    left: 43px;
    font-weight: 700;
    font-size: 44px;
    line-height: 1.22;
  }
  .headline span { display: block; }
  .headline .accent-lime { color: var(--lime); }
  .headline .accent-blue { color: var(--blue); }
  .rule {
    position: absolute;
    top: 454px;
    left: 43px;
    width: 351px;
    height: 2px;
    background: var(--white);
  }
  .standard-name {
    position: absolute;
    top: 470px;
    left: 43px;
    font-weight: 400;
    font-size: 24px;
    letter-spacing: 0.3px;
  }
  .world-map {
    position: absolute;
    top: 540px;
    left: 0;
    width: 490px;
    height: 230px;
    background: radial-gradient(ellipse at 55% 45%, var(--map-light) 0%, var(--map-mid) 45%, rgba(121,195,227,0) 72%);
    opacity: 0.85;
  }
  .tagline {
    position: absolute;
    top: 798px;
    left: 43px;
    right: 20px;
    font-size: 18.5px;
    line-height: 1.25;
    letter-spacing: 0.3px;
  }
  .contact-band {
    position: absolute;
    top: 878px;
    left: 0;
    width: 100%;
    height: 88px;
    background: var(--band);
    padding: 10px 43px 0;
    font-weight: 700;
    font-size: 25px;
    line-height: 1.4;
  }
  .contact-band .email { color: var(--lime); display: block; }
  .contact-band .web { color: var(--blue); display: block; }
  .mailing {
    position: absolute;
    top: 984px;
    left: 0; right: 0;
    text-align: center;
  }
  .mailing-title {
    color: var(--lime);
    font-weight: 700;
    font-size: 14px;
    margin-bottom: 8px;
  }
  .mailing-text {
    font-size: 13.5px;
    line-height: 1.3;
    padding: 0 24px;
  }
  .qr-frame {
    display: block;
    width: 92px;
    height: 92px;
    margin: 12px auto 0;
    border: 2px solid var(--lime);
    border-radius: 8px;
    background: var(--white);
  }
</style>
</head>
<body>
  <main class="banner">
    <div class="brand-name">csln</div>

    <h1 class="headline">
      <span>Mapping the</span>
      <span class="accent-lime">world's Internet</span>
      <span class="accent-blue">backbone.</span>
    </h1>
    <div class="rule"></div>
    <p class="standard-name">Civic Strand Ledger Norm</p>

    <div class="world-map" role="img" aria-label="Glowing light-blue world map with connection arcs linking cities across continents"></div>

    <p class="tagline">A community-driven solution for mapping the world's Internet backbone</p>

    <div class="contact-band">
      <span class="email">outreach@cslnorm.net</span>
      <span class="web">www.cslnorm.net</span>
    </div>

    <div class="mailing">
      <p class="mailing-title">Join the CSLN Mailing List</p>
      <p class="mailing-text">To stay up to date with and contribute to the development<br>and adoption of CSLN.</p>
      <div class="qr-frame" role="img" aria-label="Frame reserved for the mailing list QR code"></div>
    </div>
  </main>
</body>
</html>
```